VoxMend needs a Letterhead

We need a letterhead for our company "VoxMend Consultants". Logo is attached. The company color is Turquoise. Icons for website, scan logo for website, icons for address, e-mail and phone appreciated rather than just words.

Industry/Entity Type

It Company

```html
<!DOCTYPE html>
<html lang="en">
<head>
<meta charset="utf-8">
<title>VoxMend Consultants Letterhead</title>
<link rel="stylesheet" href="https://fonts.googleapis.com/css2?family=Open+Sans:wght@400;600&family=Tinos:wght@400;700&display=swap">
<style>
  :root {
    --paper: #ffffff;
    --brand-blue: #2f78b7;
    --brand-green: #8cc152;
    --text: #4a4a4a;
    --text-dark: #2b2b2b;
    --rule: #9bb7d4;
    --signature-tone: #eef0f2;
    --band-1: #6baad8;
    --band-2: #5a9acb;
    --band-3: #4987bf;
    --band-4: #3d72a6;
    --band-5: #2f5e8b;
  }
  * { box-sizing: border-box; margin: 0; padding: 0; }
  html, body { width: 942px; height: 1200px; overflow: hidden; background: var(--paper); }
  .letterhead {
    position: relative;
    width: 942px;
    height: 1200px;
    background: var(--paper);
    font-family: "Tinos", "Times New Roman", serif;
    color: var(--text);
  }
  .brand {
    position: absolute;
    top: 96px;
    right: 81px;
    display: flex;
    align-items: center;
    gap: 14px;
  }
  .brand-mark {
    width: 44px;
    height: 44px;
    background: var(--brand-blue);
  }
  .brand-name {
    font-family: "Open Sans", Arial, sans-serif;
    font-weight: 400;
    font-size: 30px;
    letter-spacing: 0.2px;
    color: var(--brand-blue);
  }
  .meta {
    position: absolute;
    top: 354px;
    left: 125px;
    font-size: 11.5px;
    line-height: 24px;
    color: var(--text-dark);
  }
  .meta strong { font-weight: 700; }
  .letter-body {
    position: absolute;
    top: 426px;
    left: 125px;
    width: 736px;
    font-size: 11.5px;
    line-height: 25px;
    text-align: justify;
  }
  .salutation { color: var(--text-dark); }
  .letter-body p { margin-bottom: 23px; }
  .sign-off {
    position: absolute;
    top: 834px;
    left: 125px;
    font-size: 11.5px;
    line-height: 16px;
    color: var(--text-dark);
  }
  .signature {
    position: absolute;
    top: 893px;
    left: 127px;
    width: 250px;
    height: 118px;
    background: var(--signature-tone);
    border-radius: 6px;
  }
  .contact {
    position: absolute;
    top: 1068px;
    left: 46px;
    font-family: "Open Sans", Arial, sans-serif;
    font-size: 14px;
    color: var(--brand-blue);
  }
  .contact-list { list-style: none; border-left: 1px solid var(--rule); margin-left: 27px; padding-left: 12px; }
  .contact-item { position: relative; height: 20px; line-height: 20px; }
  .contact-item svg {
    position: absolute;
    left: -35px;
    top: 4px;
    width: 13px;
    height: 13px;
    fill: var(--brand-blue);
  }
  .footer-band {
    position: absolute;
    left: 0;
    bottom: 0;
    width: 942px;
    height: 10px;
    display: flex;
  }
  .footer-band span { flex: 1; }
  .footer-band span:nth-child(1) { background: var(--band-1); }
  .footer-band span:nth-child(2) { background: var(--band-2); }
  .footer-band span:nth-child(3) { background: var(--band-3); }
  .footer-band span:nth-child(4) { background: var(--band-4); }
  .footer-band span:nth-child(5) { background: var(--band-5); }
</style>
</head>
<body>
<main class="letterhead">
  <header class="brand">
    <div class="brand-mark"></div>
    <div class="brand-name">VoxMend Consultants</div>
  </header>

  <section class="meta">
    <div><strong>Data :</strong> Mon , 25 / 3 / 2013</div>
    <div><strong>Recipient :</strong> Mr. Alan Quill Brenner</div>
  </section>

  <section class="letter-body">
    <div class="salutation">Dear Mr. Alan Quill</div>
    <p>Lorem ipsum dolor sit amet, consectetur adipiscing elit. Praesent vulputate, neque ac accumsan suscipit, justo turpis volutpat nisl, tempus fermentum eros tortor et elit. Vivamus porttitor faucibus gravida. Quisque pharetra gravida luctus. Donec eget turpis libero. Ut ac dolor urna, quis tempor nunc. Donec vitae mauris purus, euismod eleifend nulla. Lorem ipsum dolor sit amet, consectetur adipiscing elit. Donec ut purus tellus. Aenean quis dignissim lacus. Vestibulum suscipit vehicula cursus. Suspendisse potenti. Ut in sem nisi. Sed et massa leo.</p>
    <p>Fusce varius libero vel risus condimentum suscipit. Nullam tristique ultrices massa a volutpat. Donec sed dictum metus. Curabitur fringilla nibh eu ligula pharetra a interdum quam aliquam. Maecenas aliquam elit eu orci rutrum molestie. Proin nisl justo, varius a volutpat nec, ultricies sed sem. Nam sit amet imperdiet sem. Phasellus vitae mauris odio. Etiam in purus dui. Etiam ultricies, ante vel iaculis sodales, arcu leo adipiscing leo, sit amet mollis dui nisi non quam.</p>
    <p>Suspendisse sagittis laoreet dolor, vitae rhoncus arcu volutpat quis. Vestibulum at placerat dolor. Vivamus eu lacus ut enim molestie consectetur. Quisque ac lorem vel orci sagittis sollicitudin. Nunc ut quam sem, quis volutpat libero. Cum sociis natoque penatibus et magnis dis parturient montes, nascetur ridiculus mus. Vestibulum ante ipsum primis in faucibus orci luctus et ultrices posuere cubilia Curae; Donec tempor velit in velit feugiat sit amet vulputate nisl posuere..</p>
  </section>

  <section class="sign-off">
    <div>ALAN QUILL</div>
    <div>General director</div>
  </section>
  <div class="signature" role="img" aria-label="Handwritten signature of the general director"></div>

  <footer class="contact">
    <ul class="contact-list">
      <li class="contact-item">
        <svg viewBox="0 0 12 12" aria-hidden="true"><path d="M6 0.5a3.8 3.8 0 0 0-3.8 3.8C2.2 7.2 6 11.5 6 11.5s3.8-4.3 3.8-7.2A3.8 3.8 0 0 0 6 0.5zm0 5.3a1.5 1.5 0 1 1 0-3 1.5 1.5 0 0 1 0 3z"/></svg>
        48 Harbour Lane
      </li>
      <li class="contact-item">Fernvale, 40317</li>
      <li class="contact-item">
        <svg viewBox="0 0 12 12" aria-hidden="true"><path d="M1 3.2C1 2 2.5 1 6 1s5 1 5 2.2V4.5H8.3V3.4H3.7v1.1H1zM2.5 5h7l1 5.5h-9zM6 6.3a1.6 1.6 0 1 0 0 3.2 1.6 1.6 0 0 0 0-3.2z"/></svg>
        555 210 8843
      </li>
      <li class="contact-item">
        <svg viewBox="0 0 12 12" aria-hidden="true"><path d="M0.5 2.5h11v1L6 7 0.5 3.5zM0.5 4.8L6 8.3l5.5-3.5v4.7h-11z"/></svg>
        info@voxmend.com
      </li>
      <li class="contact-item">
        <svg viewBox="0 0 12 12" aria-hidden="true"><path d="M6 0.5a5.5 5.5 0 1 0 0 11 5.5 5.5 0 0 0 0-11zM1.6 5.3h2.2c.1-1.5.4-2.8.9-3.6A4.5 4.5 0 0 0 1.6 5.3zm0 1.4a4.5 4.5 0 0 0 3.1 3.6c-.5-.8-.8-2.1-.9-3.6zm3.6 0c.1 1.9.5 3.4.8 3.7.3-.3.7-1.8.8-3.7zm0-1.4h1.6C6.7 3.4 6.3 1.9 6 1.6c-.3.3-.7 1.8-.8 3.7zm3 0h2.2a4.5 4.5 0 0 0-3.1-3.6c.5.8.8 2.1.9 3.6zm0 1.4c-.1 1.5-.4 2.8-.9 3.6a4.5 4.5 0 0 0 3.1-3.6z"/></svg>
        www.voxmend.com
      </li>
    </ul>
  </footer>

  <div class="footer-band"><span></span><span></span><span></span><span></span><span></span></div>
</main>
</body>
</html>
```